Business Card Design Project

looking for a stylish and simple double sided business card.
I am an artist - specialising in fashion illustration, portraits and murals.
the front should be simply my name and tag:

D U R E S K
Living in colour

My preference is for a Black background with DURESK in red or embossed.
Living in colour in White or multi-coloured.

the back will have detail:

Personalised Art
Portraits, Murals, Fashion Illustration

0437 582 190
duresk@duresk.com.au
www.duresk.com.au

Target Market(s)

Adults that are based in western speaking countries who have an appreciation for art and design. Portraits and wall art
Business owners who may need personalised all art for their business space. Murals and personalised canvass.
People in the fashion industry, who may require fashion illustrations.

Industry/Entity Type

Fashion

Requirements
Must have
• BOLD but simple at the same time, timeless modern element to it.
Nice to have
• simple lettering
Should not have
• Not too busy or wordy,

```html
<!DOCTYPE html>
<html lang="en">
<head>
<meta charset="utf-8">
<title>Duresk – Business Card</title>
<link rel="stylesheet" href="https://fonts.googleapis.com/css2?family=Arimo:ital,wght@0,400;1,400&display=swap">
<style>
  :root {
    --sheet-grey: #c4c4c4;
    --sheet-edge: #9a9a9a;
    --label: #222222;
    --card-edge: #555555;
    --red-deep: #6e0410;
    --red-bright: #b00a1e;
    --black-top: #2a2a2c;
    --black-bottom: #050505;
    --name-red: #c0101f;
    --white: #ffffff;
    --ink: #4a4a4a;
    --ink-dark: #222222;
    --divider-red: #c0101f;
  }
  * { margin: 0; padding: 0; box-sizing: border-box; }
  html, body {
    width: 1200px; height: 386px; overflow: hidden;
    background: var(--sheet-grey);
    font-family: "Arimo", Arial, sans-serif;
  }
  .sheet {
    position: relative; width: 1200px; height: 386px;
    background: var(--sheet-grey);
    border: 1px solid var(--sheet-edge);
  }
  .side-label {
    position: absolute; top: 9px;
    font-size: 15px; color: var(--label); letter-spacing: 0.2px;
  }
  .side-label--front { left: 32px; }
  .side-label--back { left: 605px; }

  .card {
    position: absolute; top: 32px; width: 561px; height: 321px;
    overflow: hidden;
  }
  .card--front { left: 33px; background: var(--black-bottom); }
  .card--back {
    left: 606px; background: var(--white);
    border: 1px solid var(--card-edge);
  }

  .front__upper {
    position: absolute; left: 0; top: 0; width: 100%; height: 162px;
    background:
      radial-gradient(ellipse 70% 90% at 50% 55%, var(--red-bright), transparent 80%),
      linear-gradient(180deg, var(--red-deep) 0%, #9a0818 60%, #8a0616 100%);
  }
  .front__lower {
    position: absolute; left: 0; top: 162px; width: 100%; height: 159px;
    background: linear-gradient(180deg, var(--black-top) 0%, #111112 60%, var(--black-bottom) 100%);
  }
  .name {
    position: absolute; left: 0; width: 100%; top: 140px;
    text-align: center;
    font-size: 50px; line-height: 1; font-weight: 400;
    color: var(--name-red); letter-spacing: 1px;
  }
  .tagline {
    position: absolute; left: 0; width: 100%; top: 200px;
    text-align: center;
    font-size: 14px; color: var(--white); letter-spacing: 0.2px;
  }

  .divider {
    position: absolute; left: 279px; top: 62px; width: 2px; height: 196px;
    background: linear-gradient(180deg, transparent, var(--divider-red) 35%, var(--divider-red) 65%, transparent);
  }
  .services {
    position: absolute; right: 297px; top: 114px;
    text-align: right; color: var(--ink);
    font-size: 15px; line-height: 21px;
  }
  .services__lead { font-style: italic; margin-bottom: 1px; }
  .contact {
    position: absolute; left: 292px; top: 116px;
    list-style: none; color: var(--ink);
    font-size: 15px; line-height: 30px;
  }
  .contact__key {
    display: inline-block; width: 17px;
    color: var(--ink-dark);
  }
</style>
</head>
<body>
<div class="sheet">
  <div class="side-label side-label--front">FRONT</div>
  <div class="side-label side-label--back">BACK</div>

  <section class="card card--front" aria-label="Card front">
    <div class="front__upper"></div>
    <div class="front__lower"></div>
    <h1 class="name">DURESK</h1>
    <p class="tagline">Living in colour</p>
  </section>

  <section class="card card--back" aria-label="Card back">
    <div class="services">
      <p class="services__lead">Personalised Art</p>
      <p>Portraits</p>
      <p>Murals</p>
      <p>Fashion Illustration</p>
    </div>
    <div class="divider"></div>
    <ul class="contact">
      <li><span class="contact__key">t</span>0437 582 190</li>
      <li><span class="contact__key">e</span>duresk@duresk.com.au</li>
      <li><span class="contact__key">w</span>www.duresk.com.au</li>
    </ul>
  </section>
</div>
</body>
</html>
```